TQRV Brochure

I need a one or two page brochure and I have attached the content, color pallet, format samples mimic and a couple jpeg's that are optional.

Feel free to use your judgement for graphics and style but adhere to the color schema and use our content.

Colors: You can use additional grey's, if needed.
#e23232 red
#636466 Grey
#434445 Dark grey

```html
<!DOCTYPE html>
<html lang="en">
<head>
<meta charset="utf-8">
<title>TQRV Readiness Assessment Brochure</title>
<link rel="stylesheet" href="https://fonts.googleapis.com/css2?family=Poppins:wght@400;500;600;700;800&display=swap">
<style>
:root{
  --red:#e23232;
  --red-deep:#b9141a;
  --grey:#636466;
  --dark:#434445;
  --ink:#1d1d1f;
  --paper:#f4f4f4;
  --bar:#e4e4e5;
  --stage:#bfc0c2;
  --badge:#5a55a8;
}
*{box-sizing:border-box;margin:0;padding:0}
html,body{width:1200px;height:2681px;overflow:hidden}
body{background:var(--stage);font-family:'Poppins',sans-serif;color:var(--ink);position:relative}
.page{position:absolute;left:166px;width:868px;height:1123px;background:linear-gradient(125deg,#fafafa 0%,#efefef 45%,#f8f8f8 60%,#ececec 100%);overflow:hidden}
.page-one{top:132px}
.page-two{top:1396px}
.header-shape{position:absolute;left:0;top:0}
.header-photo{position:absolute;left:330px;top:0;width:538px;height:400px;background:linear-gradient(90deg,rgba(210,20,26,1) 0%,rgba(160,20,30,.75) 30%,#3a2a33 60%,#1f3550 100%)}
.header-glow{position:absolute;left:0;top:0;width:868px;height:272px;background:radial-gradient(circle at 420px 160px,rgba(255,120,120,.35) 0,rgba(226,50,50,0) 180px)}
.title{position:absolute;left:55px;color:#fff;font-weight:800;letter-spacing:.5px}
.page-one .title{top:34px;font-size:64px;line-height:60px}
.page-two .title{top:42px;font-size:50px;line-height:56px;white-space:nowrap}
.title-rule{position:absolute;left:55px;height:2px;background:#fff}
.title-rule::before{content:"";position:absolute;left:-4px;top:-4px;width:10px;height:10px;border-radius:50%;background:#fff}
.intro{position:absolute;left:55px;color:#fff;font-size:13.6px;line-height:19px}
.intro strong{font-weight:700}
h2{position:absolute;left:55px;font-size:30px;font-weight:700;color:var(--dark);white-space:nowrap}
h2 em{font-style:normal;color:var(--red)}
.body-copy{position:absolute;left:55px;width:760px;font-size:13.3px;line-height:20px;text-align:justify;color:var(--ink)}
.badge-placeholder{position:absolute;left:88px;top:712px;width:250px;height:250px;border-radius:50%;background:linear-gradient(160deg,#6a66b8 0%,var(--badge) 60%,#3f3d8c 100%)}
.arc{position:absolute;left:340px;top:660px}
.step-num{position:absolute;font-size:30px;font-weight:700;color:var(--red)}
.step-icon{position:absolute;width:92px;height:92px;border-radius:50%;border:2px solid var(--red);background:#fff;padding:4px}
.step-icon svg{display:block;width:80px;height:80px}
.step-label{position:absolute;font-size:19px;font-weight:600;color:var(--dark);line-height:23px}
.corner-trace{position:absolute;right:0;bottom:92px}
.cta-band{position:absolute;left:0;top:1036px;width:868px;height:52px;background:#1e1e1e;color:#fff;font-size:20.5px;font-weight:600;letter-spacing:.4px;text-align:center;line-height:52px;white-space:nowrap}
.contact-strip{position:absolute;left:0;top:1088px;width:868px;height:35px;background:var(--red);color:#fff;font-size:10.4px;line-height:35px;letter-spacing:.3px;padding-left:51px;white-space:nowrap}
.contact-strip b{font-weight:700}
.contact-strip .sep{margin:0 22px}
.lead{position:absolute;left:55px;font-size:17px;line-height:26px;color:var(--ink);width:700px}
.lead b{font-weight:700}
.lead em{font-style:normal;color:var(--red);font-weight:600}
.divider{position:absolute;left:55px;top:466px;width:760px;border-top:1.5px dashed #b3b3b3}
.perk{position:absolute;left:57px;width:758px;height:82px}
.perk-bar{position:absolute;left:80px;top:10px;width:678px;height:63px;background:var(--bar);border-radius:0 8px 8px 0}
.perk-icon{position:absolute;left:0;top:0;width:82px;height:82px;border-radius:8px}
.perk-icon.dark{background:var(--dark)}
.perk-icon.red{background:var(--red)}
.perk-icon svg{display:block;margin:17px;width:48px;height:48px}
.perk-label{position:absolute;left:103px;top:0;line-height:82px;font-size:18px;font-weight:600;color:var(--ink);white-space:nowrap}
</style>
</head>
<body>

<section class="page page-one">
  <div class="header-photo" role="img" aria-label="Photo of hands typing on a laptop with floating security icons and a padlock shield"></div>
  <svg class="header-shape" width="868" height="400" viewBox="0 0 868 400">
    <defs>
      <linearGradient id="redFade1" x1="0" x2="1">
        <stop offset="0" stop-color="#d5171c"/>
        <stop offset=".5" stop-color="#d5171c"/>
        <stop offset=".75" stop-color="#d5171c" stop-opacity="0"/>
      </linearGradient>
    </defs>
    <polygon points="0,0 868,0 868,400 355,400 312,360 0,360" fill="url(#redFade1)"/>
    <polygon points="0,360 312,360 355,400 0,400" fill="#f6f6f6"/>
    <path d="M0,362 H294 L328,396" fill="none" stroke="#555" stroke-width="1.5"/>
    <circle cx="328" cy="398" r="3" fill="#fff" stroke="#555" stroke-width="1.5"/>
    <line x1="0" y1="378" x2="140" y2="378" stroke="var(--red)" stroke-width="2"/>
  </svg>
  <h1 class="title">TQRV<br>READINESS<br>ASSESSMENT</h1>
  <div class="title-rule" style="top:233px;width:405px"></div>
  <p class="intro" style="top:253px;width:410px">All vendors who aspire to work within the supply chain of the U.S. Department of Defense (DoD) are required to comply with the Trusted Quality Readiness Verification (TQRV). <strong>Deadlines are approaching rapidly.</strong></p>

  <h2 style="top:438px">Why does <em>TQRV Certification</em> Matter?</h2>
  <p class="body-copy" style="top:490px">The Trusted Quality Readiness Verification (TQRV) is designed to support businesses protect sensitive data from intellectual property theft. With cybersecurity being a key priority for the U.S. Department of Defense (DoD), TQRV Certification is a mandatory requirement starting 2024 for all vendors who aspire to bid on contracts and work within the supply chain of the DoD. The various levels of the TQRV assure the DoD that the processes and practices followed by the vendor ensure the safety of Controlled Unclassified Information (CUI) and Federal Contract Information (FCI) and the flow of that information.</p>

  <h2 style="top:643px"><em>3 step</em> process...</h2>

  <div class="badge-placeholder" role="img" aria-label="Certification badge"></div>

  <svg class="arc" width="200" height="300" viewBox="0 0 200 300">
    <path d="M8,18 Q95,150 8,282" fill="none" stroke="var(--red)" stroke-width="2"/>
    <line x1="30" y1="48" x2="98" y2="26" stroke="var(--red)" stroke-width="2"/>
    <line x1="52" y1="140" x2="130" y2="140" stroke="var(--red)" stroke-width="2"/>
    <line x1="30" y1="252" x2="98" y2="268" stroke="var(--red)" stroke-width="2"/>
    <g fill="#fff" stroke="#666" stroke-width="1.5">
      <circle cx="30" cy="48" r="4"/><circle cx="98" cy="26" r="4"/>
      <circle cx="52" cy="140" r="4"/><circle cx="130" cy="140" r="4"/>
      <circle cx="30" cy="252" r="4"/><circle cx="98" cy="268" r="4"/>
    </g>
  </svg>

  <span class="step-num" style="left:442px;top:640px">1</span>
  <div class="step-icon" style="left:464px;top:662px">
    <svg viewBox="0 0 80 80"><circle cx="40" cy="40" r="40" fill="#1e1e1e"/><g fill="none" stroke="#fff" stroke-width="2"><rect x="20" y="24" width="36" height="28" rx="2"/><line x1="20" y1="30" x2="56" y2="30"/><circle cx="46" cy="46" r="8"/><line x1="52" y1="52" x2="59" y2="59"/><path d="M26 46v-6M31 46v-10M36 46v-4"/></g></svg>
  </div>
  <div class="step-label" style="left:572px;top:695px">Gap Analysis</div>

  <span class="step-num" style="left:476px;top:760px">2</span>
  <div class="step-icon" style="left:498px;top:784px">
    <svg viewBox="0 0 80 80"><circle cx="40" cy="40" r="40" fill="#1e1e1e"/><g fill="none" stroke="#fff" stroke-width="2"><circle cx="40" cy="40" r="12"/><circle cx="40" cy="40" r="5"/><path d="M40 22v6M40 52v6M22 40h6M52 40h6M27 27l4 4M49 49l4 4M27 53l4-4M49 31l4-4"/></g></svg>
  </div>
  <div class="step-label" style="left:605px;top:810px">Implement solutions<br>to meet requirements</div>

  <span class="step-num" style="left:446px;top:870px">3</span>
  <div class="step-icon" style="left:464px;top:907px">
    <svg viewBox="0 0 80 80"><circle cx="40" cy="40" r="40" fill="#1e1e1e"/><g fill="none" stroke="#fff" stroke-width="2"><rect x="18" y="24" width="40" height="30" rx="2"/><line x1="24" y1="32" x2="40" y2="32"/><line x1="24" y1="38" x2="38" y2="38"/><line x1="24" y1="44" x2="36" y2="44"/><circle cx="52" cy="40" r="6"/><path d="M48 45l-2 12 6-3 6 3-2-12"/></g></svg>
  </div>
  <div class="step-label" style="left:572px;top:940px">Get certified</div>

  <svg class="corner-trace" width="170" height="40" viewBox="0 0 170 40">
    <circle cx="4" cy="4" r="3" fill="#fff" stroke="#555" stroke-width="1.5"/>
    <path d="M6,6 L34,34 H170" fill="none" stroke="#555" stroke-width="1.5"/>
    <line x1="64" y1="26" x2="170" y2="26" stroke="var(--red)" stroke-width="2"/>
  </svg>

  <div class="cta-band">FOR A DISCUSSION OR FREE CONSULTATION, CALL US AT 555-010-4400</div>
  <div class="contact-strip">Harbor Point Tech IT Services 820 Meridian Way Ste. 14 Bayport, VA 23000<span class="sep">|</span>INFO PH <b>555-010-4400</b><span class="sep">|</span>FX <b>555-010-4401</b></div>
</section>

<section class="page page-two">
  <svg class="header-shape" width="868" height="272" viewBox="0 0 868 272">
    <defs>
      <linearGradient id="redFade2" x1="0" x2="1">
        <stop offset="0" stop-color="#d9181d"/>
        <stop offset=".5" stop-color="#c9151c"/>
        <stop offset="1" stop-color="#d51a1f"/>
      </linearGradient>
    </defs>
    <polygon points="0,0 868,0 868,272 355,272 312,232 0,232" fill="url(#redFade2)"/>
    <path d="M0,234 H294 L328,268" fill="none" stroke="#555" stroke-width="1.5"/>
    <circle cx="328" cy="270" r="3" fill="#fff" stroke="#555" stroke-width="1.5"/>
    <line x1="0" y1="250" x2="140" y2="250" stroke="var(--red)" stroke-width="2"/>
  </svg>
  <div class="header-glow" role="img" aria-label="Faint digital padlock and circuit background"></div>
  <h1 class="title">TQRV READINESS ASSESSMENT</h1>
  <div class="title-rule" style="top:120px;width:405px"></div>
  <p class="intro" style="top:143px;width:775px">All vendors who aspire to work within the supply chain of the U.S. Department of Defense (DoD) are required to comply with the Trusted Quality Readiness Verification (TQRV). <strong>Deadlines are approaching rapidly.</strong></p>

  <h2 style="top:300px">How to <em>get started...</em></h2>
  <p class="lead" style="top:350px">Call Harbor Point Tech to discuss options at <b>555-010-4400</b>.</p>
  <p class="lead" style="top:380px">Don’t hesitate as there will be a rush to certification as enforcement nears and many will be left without resources.</p>
  <div class="divider"></div>

  <h2 style="top:493px">Why <em>Harbor Point Tech</em>...</h2>
  <p class="lead" style="top:543px">Simply put, we offer a better solution at a better price.</p>

  <div class="perk" style="top:592px">
    <div class="perk-bar"></div>
    <div class="perk-icon dark"><svg viewBox="0 0 48 48" fill="none" stroke="#fff" stroke-width="2"><circle cx="32" cy="14" r="9"/><circle cx="32" cy="14" r="4"/><path d="M6 38l12-5-12-5 3 5z"/><path d="M14 14h10M20 33h20"/></svg></div>
    <div class="perk-label">Fully Inclusive TQRV Strategy</div>
  </div>
  <div class="perk" style="top:683px">
    <div class="perk-bar"></div>
    <div class="perk-icon red"><svg viewBox="0 0 48 48" fill="none" stroke="#fff" stroke-width="2"><rect x="14" y="6" width="26" height="36" rx="2"/><circle cx="12" cy="16" r="8"/><path d="M12 8v8h8"/><path d="M18 36l6-8 5 4 7-9"/></svg></div>
    <div class="perk-label">Gap Analysis, Reporting, Affordable solutions to meet requirements</div>
  </div>
  <div class="perk" style="top:774px">
    <div class="perk-bar"></div>
    <div class="perk-icon dark"><svg viewBox="0 0 48 48" fill="none" stroke="#fff" stroke-width="2"><circle cx="14" cy="26" r="5"/><circle cx="34" cy="26" r="5"/><circle cx="24" cy="30" r="5"/><path d="M5 42c0-6 4-9 9-9M43 42c0-6-4-9-9-9M15 44c0-6 4-9 9-9s9 3 9 9"/><path d="M24 4l2 4 4 .5-3 3 1 4-4-2-4 2 1-4-3-3 4-.5z"/></svg></div>
    <div class="perk-label">Experienced and Certified Consultants</div>
  </div>
  <div class="perk" style="top:865px">
    <div class="perk-bar"></div>
    <div class="perk-icon red"><svg viewBox="0 0 48 48" fill="none" stroke="#fff" stroke-width="2"><path d="M6 16l10-4 16 4 10-4v30l-10 4-16-4-10 4z"/><path d="M24 30s-7-7-7-12a7 7 0 0114 0c0 5-7 12-7 12z"/><circle cx="24" cy="18" r="2.5"/></svg></div>
    <div class="perk-label">Local to you in Tidewater Bay, Virginia</div>
  </div>

  <p class="lead" style="top:967px">We can get you <em>TQRV certified</em> and save your money and time.</p>

  <svg class="corner-trace" width="170" height="40" viewBox="0 0 170 40">
    <circle cx="4" cy="4" r="3" fill="#fff" stroke="#555" stroke-width="1.5"/>
    <path d="M6,6 L34,34 H170" fill="none" stroke="#555" stroke-width="1.5"/>
    <line x1="64" y1="26" x2="170" y2="26" stroke="var(--red)" stroke-width="2"/>
  </svg>

  <div class="cta-band">FOR A DISCUSSION OR FREE CONSULTATION, CALL US AT 555-010-4400</div>
  <div class="contact-strip">Harbor Point Tech IT Services 820 Meridian Way Ste. 14 Bayport, VA 23000<span class="sep">|</span>INFO PH <b>555-010-4400</b><span class="sep">|</span>FX <b>555-010-4401</b></div>
</section>

</body>
</html>
```